New Website - vantomix.com

This is what we looking for - http://www.sketchpoolery.com/design/738412
Updates

hello, im back and i want some good designs for my website.. i need really creative ideas. this is for a cellphone provider company. Vantomix mobile please provide me a good ideas and i will go with u also to program the website

Font styles to use
Sans Serif

```html
<!DOCTYPE html>
<html lang="en">
<head>
<meta charset="utf-8">
<title>Vantomix Communications</title>
<link href="https://fonts.googleapis.com/css2?family=Catamaran:wght@400;500;600&family=Mulish:wght@300;400;600&display=swap" rel="stylesheet">
<style>
:root{
  --blue:#1e9be0;
  --blue-bright:#3aa6ef;
  --dark:#1d1d1d;
  --dark-2:#2a2a2a;
  --text-grey:#8f8f8f;
  --line:#e2e2e2;
  --section-light:#eff0f2;
  --section-mid:#e4e5e7;
  --footer-text:#b5b5b5;
}
*{margin:0;padding:0;box-sizing:border-box}
html,body{width:954px;height:1200px;overflow:hidden}
body{font-family:"Mulish",sans-serif;background:#fff;position:relative;color:#333}
.abs{position:absolute}

/* utility bar */
.utility-bar{left:0;top:0;width:954px;height:26px;background:linear-gradient(#3a3a3a,#222);border-bottom:1px solid #444}
.utility-links{right:128px;top:6px;display:flex;gap:20px;font-size:9px;color:#ddd}
.utility-links span{display:flex;align-items:center;gap:5px}

/* header */
.site-header{left:0;top:26px;width:954px;height:68px;background:var(--dark)}
.brand{left:128px;top:16px;display:flex;align-items:center;gap:8px;font-family:"Catamaran",sans-serif}
.brand-mark{width:26px;height:26px;border:2px solid var(--blue-bright);border-radius:50%}
.brand-name{font-size:27px;font-weight:500;color:#fff;line-height:1}
.brand-sub{font-size:7.5px;letter-spacing:3px;color:#fff;margin-top:1px}
.main-nav{left:387px;top:0;height:68px;display:flex;font-family:"Catamaran",sans-serif;font-size:10px;color:#eee}
.main-nav a{display:flex;align-items:center;padding:0 12.5px;color:inherit;text-decoration:none;white-space:nowrap}
.main-nav a.active{background:var(--blue-bright);width:50px;justify-content:center;padding:0}
.search-btn{left:806px;top:25px;width:20px;height:20px;background:var(--blue-bright)}

/* hero */
.hero-photo{left:0;top:94px;width:954px;height:396px;background:linear-gradient(100deg,#e9eef2 0%,#c9ced3 30%,#d8dde1 55%,#a89a92 75%,#3a3230 100%)}
.welcome-panel{left:128px;top:210px;width:341px;height:137px;background:rgba(32,32,32,.9);padding:18px 26px 0}
.welcome-title{font-family:"Catamaran",sans-serif;font-size:25px;font-weight:400;color:#fff;line-height:32px;white-space:nowrap;padding-bottom:8px;border-bottom:1px solid #bbb}
.welcome-title em{font-style:normal;color:var(--blue-bright)}
.welcome-text{margin-top:14px;font-size:10.4px;line-height:15px;color:#f2f2f2;letter-spacing:-.1px}
.learn-btn{left:129px;top:347px;width:119px;height:32px;background:var(--blue-bright);color:#fff;font-family:"Catamaran",sans-serif;font-size:14px;display:flex;align-items:center;padding-left:25px}

/* intro */
.intro{left:0;top:490px;width:954px;height:223px;background:var(--section-light)}
.video-frame{left:128px;top:530px;width:226px;height:142px;background:linear-gradient(120deg,#2c2c2c,#6b6b6b 45%,#b9b9b9 70%,#555);border:1px solid #ccc}
.video-controls{left:0;bottom:0;width:100%;height:11px;background:#111;font-size:4px;color:#ccc;padding:3px 32px}
.play-btn{left:94px;top:53px;width:36px;height:36px;border-radius:50%;background:#d51f1f}
.intro-title{left:370px;top:530px;font-family:"Catamaran",sans-serif;font-size:19px;font-weight:500;color:var(--blue);white-space:nowrap}
.intro-text{left:370px;top:561px;width:457px;font-size:10.2px;line-height:14.4px;color:var(--text-grey);font-weight:300}
.read-more{left:370px;top:654px;font-family:"Catamaran",sans-serif;font-size:13.5px;color:var(--blue)}

/* features */
.features{left:0;top:713px;width:954px;height:355px;background:var(--section-mid)}
.card{top:755px;width:224px;height:265px;background:#f7f7f7;border-bottom:3px solid #cfcfcf}
.card.highlight{border-bottom-color:var(--blue)}
.card-photo{position:absolute;left:0;top:0;width:224px;height:155px}
.card-caption{position:absolute;left:0;top:127px;width:224px;height:28px;background:rgba(25,25,25,.85);color:#fff;font-family:"Catamaran",sans-serif;font-size:15px;padding:3px 13px;white-space:nowrap}
.card.highlight .card-caption{background:rgba(30,155,224,.92)}
.card-caption small{font-size:9px;margin-left:2px}
.card-list{position:absolute;left:10px;top:167px;width:204px;list-style:none;font-size:8.4px;color:#8a8a8a}
.card-list li{height:20.5px;line-height:17px;border-bottom:1px solid var(--line);padding-left:12px;position:relative;white-space:nowrap}
.card-list li:last-child{border-bottom:none}
.card-list li::before{content:"›";position:absolute;left:2px;top:0;color:#999}
.card-list li.link{color:var(--blue)}
.card-list li.wrap{white-space:normal}
.number-row{display:flex;gap:1px;margin:4px 0 8px 10px;align-items:center}
.number-row span{width:42px;height:21px;background:#fff;border:1px solid #ddd}
.go-btn{width:37px!important;height:21px;background:var(--blue)!important;border:none!important;margin-left:7px;color:#fff;font-size:11px;display:flex;align-items:center;justify-content:center}

/* footer */
.site-footer{left:0;top:1068px;width:954px;height:100px;background:#262626}
.footer-heading{font-family:"Catamaran",sans-serif;font-size:14px;color:#bbb;padding-bottom:8px;border-bottom:1px solid #444}
.quick-links{left:128px;top:1092px;width:358px}
.footer-nav{margin-top:8px;display:flex;gap:12px;font-size:10px;color:var(--footer-text);white-space:nowrap}
.footer-nav span{flex:none}
.follow{left:690px;top:1092px;width:136px}
.social-row{margin-top:10px;display:flex;gap:6px;justify-content:flex-end}
.social-row span{width:11px;height:11px;border-radius:50%;background:#999}
.legal-bar{left:0;top:1168px;width:954px;height:32px;background:#efefef;font-size:9px;color:#999;text-align:center;line-height:32px}
</style>
</head>
<body>

<div class="abs utility-bar"></div>
<div class="abs utility-links">
  <span><svg width="8" height="8" viewBox="0 0 8 8"><circle cx="4" cy="2.3" r="2" fill="#ddd"/><path d="M0 8a4 3 0 0 1 8 0z" fill="#ddd"/></svg>My Account</span>
  <span><svg width="9" height="8" viewBox="0 0 9 8"><rect x="0" y="4" width="6" height="4" fill="#ddd"/><path d="M4 4V2a2 2 0 0 1 4 0" stroke="#ddd" fill="none"/></svg>Log In</span>
  <span><svg width="8" height="8" viewBox="0 0 8 8"><path d="M1 5a3 3 0 0 1 6 0" stroke="#ddd" fill="none"/><rect x="0.5" y="4.5" width="2" height="3" fill="#ddd"/><rect x="5.5" y="4.5" width="2" height="3" fill="#ddd"/></svg>Live Chat</span>
</div>

<header class="abs site-header">
  <div class="abs brand">
    <div class="brand-mark"></div>
    <div>
      <div class="brand-name">Vantomix</div>
      <div class="brand-sub">COMMUNICATIONS</div>
    </div>
  </div>
  <nav class="abs main-nav">
    <a class="active">HOME</a><a>ABOUT US</a><a>OFFICE</a><a>CELLPHONE</a><a>SUPPORT</a><a>CONTACT US</a>
  </nav>
  <div class="abs search-btn"><svg width="20" height="20" viewBox="0 0 20 20"><circle cx="9" cy="9" r="3.5" stroke="#fff" stroke-width="1.6" fill="none"/><path d="M11.5 11.5l3 3" stroke="#fff" stroke-width="1.8"/></svg></div>
</header>

<div class="abs hero-photo" role="img" aria-label="Photo of smiling call-centre agents wearing headsets in a bright office"></div>
<div class="abs welcome-panel">
  <h1 class="welcome-title">WELCOME TO VANTO<em>MIX</em></h1>
  <p class="welcome-text">Lorem Ipsum is simply dummy text of typesetting industry. Lorem Ipsum has been the industry's standard dummy text ever since the 1500s.</p>
</div>
<div class="abs learn-btn">Learn More</div>

<section class="abs intro"></section>
<div class="abs video-frame" role="img" aria-label="Video still of a woman on the phone at an office desk">
  <div class="abs play-btn"><svg width="36" height="36" viewBox="0 0 36 36"><path d="M14 10l11 8-11 8z" fill="#fff"/></svg></div>
  <div class="abs video-controls">0:00</div>
</div>
<h2 class="abs intro-title">This is Pixelcraft's version &nbsp;of Lorem Ipsum.</h2>
<p class="abs intro-text">Lorem Ipsum is simply dummy text of the printing and typesetting industry. Lorem Ipsum has been the industry's standard dummy text ever since the 1500s, when an unknown printer took a galley of type and scrambled it to make a type specimen book. It has survived not only five centuries, but also the leap into electronic typesetting, remaining essentially unchanged. It was popularised in the 1960s with the release of Typeline sheets containing Lorem Ipsum passages, and more recently with desktop publishing software like Pagewright Studio including versions of Lorem</p>
<div class="abs read-more">Read More »</div>

<section class="abs features"></section>

<article class="abs card" style="left:128px">
  <div class="card-photo" role="img" aria-label="Photo of a hand dropping a coin into a yellow smiley piggy bank" style="background:linear-gradient(135deg,#b9c2c4,#8f9a92 50%,#d9c23a 75%,#c9b02a)"></div>
  <div class="card-caption">AFFORDABLE <small>Start Saving Today!</small></div>
  <ul class="card-list">
    <li>Unlimited local and long distance calling</li>
    <li>5 nation unlimited interntional</li>
    <li>No set-up, equipment fees, or hidden..</li>
    <li>No contracts or commitments</li>
  </ul>
</article>

<article class="abs card highlight" style="left:365px">
  <div class="card-photo" role="img" aria-label="Photo of a speaker on stage gesturing in front of bright screens" style="background:linear-gradient(135deg,#3a2a30,#1a1a22 45%,#6a2a2a 70%,#222)"></div>
  <div class="card-caption">POWERFUL <small>Incredible Features, Standard</small></div>
  <ul class="card-list">
    <li>Seamless integration with Mailbridge</li>
    <li>Get calls and voicemail anywhere</li>
    <li>100% hurricane proof</li>
    <li class="link">Featuring the power of Linkvale!</li>
  </ul>
</article>

<article class="abs card" style="left:601px">
  <div class="card-photo" role="img" aria-label="Photo of a curved smartphone with a red screen" style="background:linear-gradient(135deg,#c8ccd0,#9ea3a8 40%,#4a2a26 65%,#b0b4b8)"></div>
  <div class="card-caption">FLEXIBLE <small>Service on your own terms</small></div>
  <ul class="card-list" style="top:157px">
    <li style="border:none">Keep Your Number</li>
  </ul>
  <div class="number-row" style="position:absolute;top:179px;left:12px"><span></span><span></span><span></span><span class="go-btn">GO</span></div>
  <ul class="card-list" style="top:208px">
    <li>Choose your own area code</li>
    <li class="wrap" style="height:32px;line-height:12px;padding-top:3px">Custom-tailored business solutions,both hosted and loccal</li>
  </ul>
</article>

<footer class="abs site-footer"></footer>
<div class="abs quick-links">
  <div class="footer-heading">Quick links</div>
  <div class="footer-nav"><span>Home</span><span>I</span><span>About Us</span><span>I</span><span>Office</span><span>I</span><span>Cellphone</span><span>I</span><span>Support</span><span>I</span><span>Contact Us</span></div>
</div>
<div class="abs follow">
  <div class="footer-heading">Follow us on</div>
  <div class="social-row"><span></span><span></span><span></span><span></span><span></span><span></span><span></span><span></span></div>
</div>
<div class="abs legal-bar">© 2014 Vantomix Communication . All Rights Reserved. Terms and Conditions</div>

</body>
</html>
```